Money Mindset Podcast needs fun, creative cover art

Launching a new podcast called 'Turning the Page on Savings' - aimed at an audience 30-50 who are interested in the practicalities of managing their money but also the more mental and emotional aspects.
Looking for something not too serious, warm and friendly.

Must be easy to read on phone screens
3000 x 3000 in size
Avoid currency symbols $, £ etc, as may have an international audience

Target Market(s)

Podcast listeners age 30-50 starting in the UK but then worldwide. Probably 60:40 female bias

Industry/Entity Type

Life Coaching

Font styles to use
Serif
Sans Serif

Colors
cadf82
fee18a
acd037
85cae6
eea4c8
f59195
85acd3

Requirements
Must have
• Simple, clear design. Easy to read on variety of devices. 3000 x 3000
Appeal to those with a spiritual or emotional interests
Nice to have
• Stand out among other money related podcasts
Maybe play around with clouds, lightbulbs and clearing skies
Should not have
• Currency symbols such as $ or £
Be too corporate or bank like
Stock images

```html
<!DOCTYPE html>
<html lang="en">
<head>
<meta charset="utf-8">
<title>Turning the Page on Savings – Podcast Cover</title>
<link rel="stylesheet" href="https://fonts.googleapis.com/css2?family=Archivo+Black&display=swap">
<style>
  :root {
    --page-bg: #ffffff;
    --sky: #85cae6;
    --sky-light: #cfeaf5;
    --butter: #fee18a;
    --cream: #fff7d6;
    --lime: #acd037;
    --mint: #cadf82;
    --pink: #eea4c8;
    --coral: #f59195;
    --slate-blue: #85acd3;
    --navy: #1c1f5c;
    --purple: #5b2d8e;
  }
  html, body {
    margin: 0;
    width: 1200px;
    height: 751px;
    overflow: hidden;
    background: var(--page-bg);
  }
  .cover {
    position: absolute;
    left: 250px;
    top: 25px;
    width: 700px;
    height: 700px;
    display: block;
  }
  .title {
    font-family: "Archivo Black", "Arial Black", sans-serif;
    fill: var(--navy);
  }
  .title--accent { fill: url(#accentInk); }
</style>
</head>
<body>
<svg class="cover" viewBox="0 0 713 713" role="img" aria-label="Podcast cover: Turning the Page on Savings">
  <defs>
    <linearGradient id="skyWash" x1="0" y1="0" x2="0" y2="1">
      <stop offset="0" stop-color="var(--sky)"/>
      <stop offset="0.5" stop-color="var(--sky-light)"/>
      <stop offset="0.78" stop-color="var(--cream)"/>
      <stop offset="1" stop-color="var(--butter)"/>
    </linearGradient>
    <radialGradient id="sunGlow" cx="0.5" cy="0.5" r="0.5">
      <stop offset="0" stop-color="var(--cream)"/>
      <stop offset="0.7" stop-color="var(--butter)"/>
      <stop offset="1" stop-color="var(--butter)" stop-opacity="0"/>
    </radialGradient>
    <linearGradient id="accentInk" x1="0" y1="0" x2="1" y2="0">
      <stop offset="0" stop-color="var(--purple)"/>
      <stop offset="1" stop-color="var(--navy)"/>
    </linearGradient>
  </defs>

  <g class="backdrop">
    <rect width="713" height="713" fill="url(#skyWash)"/>
    <circle class="sun" cx="560" cy="150" r="170" fill="url(#sunGlow)"/>
  </g>

  <g class="horizon">
    <path class="hill hill--back" d="M0 640 Q200 590 420 630 T713 610 V713 H0 Z" fill="var(--mint)"/>
    <path class="hill hill--front" d="M0 680 Q260 640 500 675 T713 665 V713 H0 Z" fill="var(--lime)"/>
  </g>

  <g class="dots" fill="var(--coral)">
    <circle cx="72" cy="92" r="10"/>
    <circle cx="640" cy="420" r="8" fill="var(--pink)"/>
    <circle cx="96" cy="600" r="7" fill="var(--slate-blue)"/>
  </g>

  <g class="headline">
    <text class="title" x="175" y="236" font-size="86" textLength="470" lengthAdjust="spacingAndGlyphs" transform="rotate(-10 175 236)">TURNING</text>
    <text class="title" x="140" y="330" font-size="96" textLength="190" lengthAdjust="spacingAndGlyphs" transform="rotate(-10 140 330)">THE</text>
    <text class="title" x="445" y="322" font-size="82" textLength="130" lengthAdjust="spacingAndGlyphs" transform="rotate(-10 445 322)">ON</text>
    <text class="title title--accent" x="52" y="488" font-size="170" textLength="355" lengthAdjust="spacingAndGlyphs" transform="rotate(-10 52 488)">PAGE</text>
    <text class="title" x="185" y="590" font-size="150" textLength="480" lengthAdjust="spacingAndGlyphs" transform="rotate(-10 185 590)">SAVINGS</text>
  </g>
</svg>
</body>
</html>
```